snugSEAL - packaging design for plastic zip-lock mechansim

Looking for packaging designs for my patented product, which provides the ability to lock and close existing plastic bags, which have been opened up (like sugar or flour bag, snack bag, etc.). With applying snugSEAL to any bag once opened, the products can be held safe, locked and dry.
Please check my supporting documentation attached, including logos and packaging description.
The packaging design has to make clear to the customer:
- WHAT is this product for
- how to USA
- what are the BENEFITS and the VALUE
I am looking for a long term cooperation with the winning designer, as I will need multiple variations of the packaging depending on individual product usage. I am thinking of approximately 10 different variations in the future.
Updates
Project Deadline Extended Reason: Extending deadline to receive more designs. Please submit your designs according to my description. Let me know if any questions!This will be a long term cooperation as I will need subsequent designs for alternative product variations in the future. Added Saturday, October 22, 2016
Target Market(s)
All consumers who buy products in the supermarket. In particular when they buy products in bags (like salt, sugar, flour, detergents, snacks, ...)
Industry/Entity Type
Retail
Look and feel
Each slider illustrates characteristics of the customer's brand and the style your logo design should communicate.

```html
<!DOCTYPE html>
<html lang="en">
<head>
<meta charset="utf-8">
<title>snugSEAL packaging – dieline</title>
<link rel="stylesheet" href="https://fonts.googleapis.com/css2?family=Anton&family=Archivo+Black&family=Arimo:wght@400;700&display=swap">
<style>
  :root {
    --paper: #ffffff;
    --ink: #231f20;
    --guide: #8a8a8a;
    --pack-yellow: #f9c614;
    --pack-yellow-deep: #f2a900;
    --pea-light: #9fd35a;
    --pea-dark: #2f7a1d;
    --brand-red: #e2141c;
    --brand-brown: #6b3b12;
    --sleeve: #eeeeef;
    --sleeve-edge: #cfcfd2;
    --swatch-cyan: #00aeef;
    --swatch-magenta: #ec008c;
    --swatch-yellow: #fff200;
    --swatch-black: #231f20;
  }
  * { box-sizing: border-box; margin: 0; padding: 0; }
  html, body { width: 891px; height: 1200px; overflow: hidden; background: var(--paper); }
  .canvas { position: relative; width: 891px; height: 1200px; overflow: hidden; background: var(--paper); font-family: "Arimo", Arial, sans-serif; color: var(--ink); }

  .dimensions { position: absolute; inset: 0; }
  .dim-label { position: absolute; font-size: 13px; color: var(--ink); white-space: nowrap; }
  .dim-label.vertical { transform: translate(-50%, -50%) rotate(-90deg); }

  /* card */
  .card { position: absolute; width: 272px; height: 419px; overflow: hidden; background: var(--pack-yellow); }
  .card-art { position: absolute; inset: 0; }
  .pack-count { position: absolute; right: 12px; top: 128px; font-family: "Anton", sans-serif; color: var(--brand-red); font-size: 38px; line-height: 1;
    text-shadow: 1px 1px 0 #fff, -1px -1px 0 #fff, 1px -1px 0 #fff, -1px 1px 0 #fff, 2px 3px 2px rgba(0,0,0,.45); }
  .pack-count small { font-size: 26px; }
  .benefits { position: absolute; left: 14px; top: 188px; font-family: "Archivo Black", sans-serif; font-size: 17px; line-height: 25px; color: #fff;
    text-shadow: 1px 1px 0 #555, 2px 2px 2px rgba(0,0,0,.5); list-style: none; }
  .usage { position: absolute; left: 182px; width: 90px; top: 188px; text-align: center; font-family: "Archivo Black", sans-serif; font-size: 11.5px; line-height: 18px; color: #fff;
    text-shadow: 1px 1px 0 #555, 2px 2px 2px rgba(0,0,0,.5); }
  .brand-name { position: absolute; left: 136px; top: 245px; transform: translate(-50%, -50%) rotate(-90deg); font-family: "Archivo Black", sans-serif; font-size: 15px; color: var(--brand-brown); white-space: nowrap; }
  .product-name { position: absolute; left: 0; right: 0; top: 304px; text-align: center; font-family: "Anton", sans-serif; color: var(--brand-red); line-height: 1;
    text-shadow: 2px 2px 0 #fff, -2px -2px 0 #fff, 2px -2px 0 #fff, -2px 2px 0 #fff, 0 2px 0 #fff, 2px 0 0 #fff, 3px 4px 3px rgba(0,0,0,.5); }
  .product-name .line-small { display: block; font-size: 40px; letter-spacing: .5px; }
  .product-name .line-big { display: block; font-size: 64px; letter-spacing: 1px; margin-top: 2px; }

  /* back */
  .card.back { transform: rotate(180deg); }
  .back-title { position: absolute; left: 0; right: 0; top: 44px; text-align: center; font-size: 17px; font-weight: 700; color: var(--ink); }
  .step { position: absolute; left: 0; right: 0; height: 84px; border-top: 2px solid #fff; display: flex; align-items: center; gap: 12px; padding-left: 20px; }
  .step-figure { width: 58px; height: 52px; background: #fff; flex: none; display: flex; align-items: center; justify-content: center; font-size: 14px; }
  .step-text { font-size: 12.5px; line-height: 15px; color: var(--ink); }

  /* side strip and sleeve */
  .side-strip { position: absolute; left: 331px; top: 22px; width: 18px; height: 419px; background: linear-gradient(to bottom, var(--pea-dark), var(--pea-light) 20%, var(--pack-yellow) 24%, var(--pack-yellow-deep)); border: 1px solid var(--sleeve-edge); }
  .side-sleeve { position: absolute; left: 331px; top: 441px; width: 18px; height: 670px; background: var(--sleeve); border: 1px solid var(--sleeve-edge); }
  .sleeve { position: absolute; left: 40px; top: 441px; width: 272px; height: 670px; background: linear-gradient(to right, var(--sleeve), #fafafa 40%, var(--sleeve)); border: 1px solid var(--sleeve-edge); }
  .sleeve-label { position: absolute; left: 0; right: 0; top: 392px; text-align: center; font-size: 14px; }

  .side-label { position: absolute; font-size: 15px; line-height: 20px; text-align: center; }

  .spec { position: absolute; left: 460px; font-size: 14px; line-height: 19px; }
  .swatches { position: absolute; left: 460px; top: 934px; list-style: none; font-size: 11px; }
  .swatches li { display: flex; align-items: center; gap: 9px; height: 20px; }
  .swatches .dot { width: 14px; height: 14px; border-radius: 50%; }
</style>
</head>
<body>
<div class="canvas">

  <!-- left: card on sleeve -->
  <div class="sleeve"><p class="sleeve-label">plastic sleeve</p></div>

  <div class="card front" style="left:40px; top:22px;">
    <svg class="card-art" width="272" height="419" viewBox="0 0 272 419">
      <defs>
        <linearGradient id="peaGrad" x1="0" y1="0" x2="0" y2="1">
          <stop offset="0" stop-color="#5aa532"/><stop offset=".6" stop-color="#8cc84b"/><stop offset="1" stop-color="#3f8a22"/>
        </linearGradient>
        <linearGradient id="yellowGrad" x1="0" y1="0" x2="0" y2="1">
          <stop offset="0" stop-color="#ffd83a"/><stop offset="1" stop-color="#f4a900"/>
        </linearGradient>
      </defs>
      <rect width="272" height="419" fill="url(#yellowGrad)"/>
      <path d="M0 0H272V92C220 100 160 120 136 172C112 120 52 100 0 92Z" fill="url(#peaGrad)" role="img" aria-label="Photo of fresh green peas spilling from an opened bag"/>
      <rect x="118" y="14" width="36" height="12" rx="6" fill="#fff"/>
      <circle cx="136" cy="27" r="8" fill="#fff"/>
    </svg>
    <p class="pack-count">5<small>pcs</small></p>
    <ul class="benefits"><li>PERFECT</li><li>SIMPLE</li><li>EASY</li></ul>
    <p class="brand-name">snugSEAL</p>
    <p class="usage">USE IN THE<br>KITCHEN<br>AND<br>ALL IN THE<br>HOUSE</p>
    <h1 class="product-name"><span class="line-small">PLASTIC BAG</span><span class="line-big">SEALER</span></h1>
  </div>

  <div class="side-strip"></div>
  <div class="side-sleeve"></div>

  <!-- right: unfolded card -->
  <div class="card back" style="left:458px; top:22px;">
    <svg class="card-art" width="272" height="419" viewBox="0 0 272 419">
      <rect width="272" height="419" fill="var(--pack-yellow)"/>
      <rect x="118" y="14" width="36" height="12" rx="6" fill="#fff"/>
      <circle cx="136" cy="27" r="8" fill="#fff"/>
    </svg>
    <h2 class="back-title">How to use</h2>
    <div class="step" style="top:82px;"><div class="step-figure"></div><p class="step-text">Lorem ipsum lorem<br>Lorem ipsum lorem<br>Lorem ipsum lorem<br>Lorem ipsum lorem</p></div>
    <div class="step" style="top:166px;"><div class="step-figure"></div><p class="step-text">Lorem ipsum lorem<br>Lorem ipsum lorem<br>Lorem ipsum lorem<br>Lorem ipsum lorem</p></div>
    <div class="step" style="top:250px;"><div class="step-figure"></div><p class="step-text">Lorem ipsum lorem<br>Lorem ipsum lorem<br>Lorem ipsum lorem<br>Lorem ipsum lorem</p></div>
    <div class="step" style="top:334px;"><div class="step-figure">code</div><p class="step-text">Lorem ipsum lorem<br>Lorem ipsum lorem<br>Lorem ipsum lorem</p></div>
  </div>

  <div class="card front" style="left:458px; top:441px; height:416px;">
    <svg class="card-art" width="272" height="419" viewBox="0 0 272 419">
      <defs>
        <linearGradient id="peaGrad2" x1="0" y1="0" x2="0" y2="1">
          <stop offset="0" stop-color="#5aa532"/><stop offset=".6" stop-color="#8cc84b"/><stop offset="1" stop-color="#3f8a22"/>
        </linearGradient>
        <linearGradient id="yellowGrad2" x1="0" y1="0" x2="0" y2="1">
          <stop offset="0" stop-color="#ffd83a"/><stop offset="1" stop-color="#f4a900"/>
        </linearGradient>
      </defs>
      <rect width="272" height="419" fill="url(#yellowGrad2)"/>
      <path d="M0 0H272V92C220 100 160 120 136 172C112 120 52 100 0 92Z" fill="url(#peaGrad2)" role="img" aria-label="Photo of fresh green peas spilling from an opened bag"/>
    </svg>
    <p class="pack-count">5<small>pcs</small></p>
    <ul class="benefits"><li>PERFECT</li><li>SIMPLE</li><li>EASY</li></ul>
    <p class="brand-name">snugSEAL</p>
    <p class="usage">USE IN THE<br>KITCHEN<br>AND<br>ALL IN THE<br>HOUSE</p>
    <h2 class="product-name"><span class="line-small">PLASTIC BAG</span><span class="line-big">SEALER</span></h2>
  </div>

  <!-- dimension lines -->
  <svg class="dimensions" width="891" height="1200" viewBox="0 0 891 1200" fill="none" stroke="var(--guide)" stroke-width="1">
    <path d="M312 22H760M312 441H470M730 441H840M350 857H470M730 857H840M312 1111H400"/>
    <path d="M40 1111V1180M312 1111V1180"/>
    <path d="M383 22V1111M431 22V441M431 441V857M40 1158H312"/>
    <g fill="var(--guide)" stroke="none">
      <path d="M383 22l-3 9h6zM383 1111l-3-9h6zM431 22l-3 9h6zM431 441l-3-9h6zM431 441l-3 9h6zM431 857l-3-9h6zM40 1158l9-3v6zM312 1158l-9-3v6z"/>
    </g>
  </svg>
  <span class="dim-label vertical" style="left:370px; top:580px;">260 mms</span>
  <span class="dim-label vertical" style="left:418px; top:245px;">100 mms</span>
  <span class="dim-label vertical" style="left:418px; top:650px;">100 mms</span>
  <span class="dim-label" style="left:148px; top:1136px;">65 mms</span>

  <p class="side-label" style="left:0; top:240px;">clip</p>
  <p class="side-label" style="left:762px; top:232px;">back<br>side</p>
  <p class="side-label" style="left:760px; top:654px;">front<br>side</p>

  <p class="spec" style="top:892px; font-size:15px;">Project: snugSEAL packaging</p>
  <ul class="swatches">
    <li><span class="dot" style="background:var(--swatch-cyan)"></span>cyan</li>
    <li><span class="dot" style="background:var(--swatch-magenta)"></span>magenta</li>
    <li><span class="dot" style="background:var(--swatch-yellow)"></span>yellow</li>
    <li><span class="dot" style="background:var(--swatch-black)"></span>black</li>
  </ul>
  <p class="spec" style="top:1054px;">Material:- cardboard 250g<br>&nbsp;&nbsp;&nbsp;&nbsp;&nbsp;&nbsp;&nbsp;&nbsp;&nbsp;&nbsp;&nbsp;&nbsp;&nbsp;&nbsp;- plastic sleeve, 60 mms wide<br>&nbsp;&nbsp;&nbsp;&nbsp;&nbsp;&nbsp;&nbsp;&nbsp;&nbsp;&nbsp;&nbsp;&nbsp;&nbsp;&nbsp;&nbsp;&nbsp;welded and&nbsp; perforated<br>&nbsp;&nbsp;&nbsp;&nbsp;&nbsp;&nbsp;&nbsp;&nbsp;&nbsp;&nbsp;&nbsp;&nbsp;&nbsp;&nbsp;&nbsp;&nbsp;á 260 mms</p>
  <p class="spec" style="top:1158px;">M=1:1</p>
</div>
</body>
</html>
```